Dulwick Medical

Need smart and sleek business cards design for my medical distribution company. use logos attached.

add my details

Harriet Colbeck
Director/Sales Agent
harriet@dulwickmedical.com.au
0461 835 207

```html
<!DOCTYPE html>
<html lang="en">
<head>
<meta charset="utf-8">
<title>Dulwick Medical — Business Cards</title>
<link href="https://fonts.googleapis.com/css2?family=Roboto:wght@400;700&display=swap" rel="stylesheet">
<style>
  :root {
    --navy: #012461;
    --sky: #2a86c4;
    --white: #ffffff;
    --ink: #333a44;
    --rule: #3a3a3a;
    --backdrop: #e6e7ea;
  }
  * { box-sizing: border-box; margin: 0; padding: 0; }
  html, body { width: 1200px; height: 880px; overflow: hidden; }
  body {
    background: var(--backdrop);
    font-family: "Roboto", Arial, sans-serif;
    display: flex;
    flex-direction: column;
    align-items: center;
    justify-content: center;
    gap: 44px;
  }
  .card {
    width: 620px;
    height: 374px;
    border-radius: 26px;
    position: relative;
    box-shadow: 0 10px 28px rgba(0,0,0,0.18);
  }
  .card--front {
    background: var(--navy);
    display: flex;
    align-items: center;
    justify-content: center;
  }
  .wordmark {
    display: flex;
    align-items: center;
    gap: 14px;
    font-weight: 700;
    color: var(--white);
  }
  .wordmark__square {
    width: 30px; height: 30px;
    background: currentColor;
  }
  .card--front .wordmark { font-size: 48px; letter-spacing: 1px; }
  .card--back { background: var(--white); }
  .card--back .wordmark {
    position: absolute;
    right: 44px; top: 46px;
    font-size: 30px;
    color: var(--navy);
    gap: 10px;
  }
  .card--back .wordmark__square { width: 20px; height: 20px; }
  .holder {
    position: absolute;
    left: 100px; top: 208px;
  }
  .holder__name {
    font-weight: 700;
    font-size: 28px;
    color: var(--navy);
  }
  .holder__title {
    font-size: 17px;
    color: var(--ink);
    margin-top: 6px;
  }
  .divider {
    position: absolute;
    left: 100px; right: 40px; top: 286px;
    height: 1px;
    background: var(--rule);
  }
  .contact {
    position: absolute;
    display: flex;
    align-items: center;
    gap: 9px;
    font-size: 17px;
    color: var(--ink);
  }
  .contact svg { width: 18px; height: 18px; fill: var(--sky); flex: none; }
  .contact--email { right: 40px; top: 256px; }
  .contact--phone { left: 100px; top: 302px; }
</style>
</head>
<body>
  <section class="card card--front" aria-label="Card front">
    <div class="wordmark"><span class="wordmark__square"></span>Dulwick Medical</div>
  </section>

  <section class="card card--back" aria-label="Card back">
    <div class="wordmark"><span class="wordmark__square"></span>Dulwick Medical</div>

    <div class="holder">
      <p class="holder__name">Harriet Colbeck</p>
      <p class="holder__title">Director/Sales Agent</p>
    </div>

    <p class="contact contact--email">
      <svg viewBox="0 0 24 24" aria-hidden="true"><path d="M2 5h20v14H2z M3.5 6.5 12 13l8.5-6.5" fill="none" stroke="#2a86c4" stroke-width="2"/><path d="M2 5h20L12 12z"/></svg>
      harriet@dulwickmedical.com.au
    </p>

    <div class="divider"></div>

    <p class="contact contact--phone">
      <svg viewBox="0 0 24 24" aria-hidden="true"><path d="M6.6 10.8a15.1 15.1 0 0 0 6.6 6.6l2.2-2.2a1 1 0 0 1 1-.25 11.4 11.4 0 0 0 3.6.57 1 1 0 0 1 1 1V20a1 1 0 0 1-1 1A17 17 0 0 1 3 4a1 1 0 0 1 1-1h3.5a1 1 0 0 1 1 1c0 1.25.2 2.45.57 3.57a1 1 0 0 1-.25 1z"/></svg>
      0461 835 207
    </p>
  </section>
</body>
</html>
```